Frontpage for an independent Forex trading tournaments website

We need a frontpage design for the first independent Forex trading tournaments platform.
Intraday Forex traders from all over the world come to this website to participate in daily contests, and if they trade better than others — win the bets. This website is the first of a kind — it is not affiliated with any type of brokers, and does not promote any broker services.
People can trade with their existing live or demo accounts (and they even can win real money with demo accounts)
The main goal of the frontpage is to explain what this website is about and make them sign up via Vendrix or Lumora buttons, or traditional email.
Attached to this project is a sample mock-up that seems reasonable, but we're open to further suggestions.
Updates
Dear designers,
Also please use bigger fonts and use don't leave too big blank spaces.
Target Market(s)
Intraday Forex traders from 24 to 34 years, mostly males, higher education, working as traders or trading as a hobby.
Mostly living in developing countries: Indonesia, Eastern Europe, Arab countries, China, Latin America.
Industry/Entity Type
Trade
Requirements
Must have
- * Clean design with clear message
* An easy-to-see way to show that we have single-click Vendrix/Lumora registration
Should not have
- * No implied javascript-animated nested menus or pop-ups, no flash — that would make the website difficult to browse on mobile devices which employ touch-based controls

```html
<!DOCTYPE html>
<html lang="en">
<head>
<meta charset="utf-8">
<title>TradeArenas.com – Forex Tournaments</title>
<link rel="stylesheet" href="https://fonts.googleapis.com/css2?family=Ubuntu:wght@400;500;700&display=swap">
<style>
:root{
  --black:#000;
  --ink:#111;
  --row:#1c1c1c;
  --row-line:#333;
  --orange:#f28a00;
  --orange-deep:#e45200;
  --orange-light:#ffb21e;
  --gold:#f7a81b;
  --white:#fff;
  --grey-text:#8a8a8a;
  --vendrix:#1f3d7a;
  --lumora:#2a9ad8;
  --text:#222;
}
*{box-sizing:border-box;margin:0;padding:0}
html,body{width:915px;height:1200px;overflow:hidden}
body{position:relative;font-family:"Ubuntu",sans-serif;background:var(--white);color:var(--text)}
.abs{position:absolute}

/* header */
.site-header{left:0;top:0;width:915px;height:80px;background:var(--black)}
.brand{left:142px;top:30px;font-size:24px;color:var(--white);font-weight:400;letter-spacing:-.5px}
.main-nav{left:386px;top:40px;display:flex;gap:26px;font-size:11px;font-weight:500;color:var(--white);letter-spacing:.3px}
.sign-in{left:738px;top:40px;font-size:11px;font-weight:500;color:var(--gold)}

/* hero */
.hero{left:0;top:80px;width:915px;height:176px;background:linear-gradient(180deg,var(--orange-light) 0%,var(--orange) 45%,var(--orange-deep) 100%)}
.hero-title{left:146px;top:114px;font-size:19px;font-weight:500;color:var(--white);letter-spacing:-.6px}
.hero-sub{left:146px;top:137px;font-size:12.5px;font-weight:500;color:var(--white)}
.join-btn{left:359px;top:174px;width:196px;height:64px;background:linear-gradient(#2a2a2a,#000);border:2px solid #555;border-radius:6px;color:var(--white);font-size:25px;font-weight:700;display:flex;align-items:center;justify-content:center;letter-spacing:-.5px;box-shadow:0 3px 4px rgba(0,0,0,.4)}

/* trust section */
.trust{left:0;top:256px;width:915px;height:254px;background:linear-gradient(180deg,#fff 0%,#f4f4f4 60%,#e2e2e2 100%);border-bottom:1px solid #ccc}
.portrait{left:128px;top:228px;width:166px;height:282px;background:radial-gradient(ellipse 70% 55% at 50% 30%,#d9c3b0 0%,#cdbfb2 45%,rgba(205,200,192,.85) 75%,rgba(226,226,226,0) 100%),linear-gradient(180deg,rgba(200,195,188,0) 0%,#c6c2bb 55%,#d6d4d0 100%);border-radius:14px 14px 0 0}
.quote{left:296px;top:314px;width:212px;height:118px;background:var(--white);border:1px solid #ddd;border-radius:8px;box-shadow:0 2px 5px rgba(0,0,0,.18);padding:11px 10px 0 12px;font-size:9.4px;line-height:12.8px;color:#333}
.quote cite{display:block;margin-top:5px;font-style:normal;color:var(--orange-deep)}
.brokers-title{left:537px;top:286px;font-size:19px;font-weight:500;color:var(--ink);letter-spacing:-.5px}
.broker-grid{left:535px;top:313px;display:grid;grid-template-columns:repeat(3,78px);grid-auto-rows:78px;gap:5px}
.broker{background:linear-gradient(#fff,#eee);border:1px solid #d6d6d6;border-radius:5px;display:flex;align-items:center;justify-content:center;font-size:11px;font-weight:500;color:#333}

/* tournaments */
.section-title{left:146px;top:519px;font-size:22px;font-weight:500;color:var(--ink);letter-spacing:-.4px}
.table-head{left:0;top:550px;width:915px;height:28px;background:linear-gradient(var(--orange-light),var(--orange));font-size:11.5px;font-weight:500;color:var(--ink)}
.table-head span{position:absolute;top:8px}
.table-head span::before{content:"";display:inline-block;border:4.5px solid transparent;border-top:5px solid var(--ink);border-bottom:0;margin-right:5px;vertical-align:2px}
.table-body{left:0;top:578px;width:915px;height:260px;background:var(--black)}
.t-rows{left:129px;top:578px;width:656px;height:200px;background:var(--row);border:1px solid #2c2c2c}
.t-row{position:absolute;left:0;width:654px;height:32px;border-bottom:1px solid var(--row-line);font-size:12px;color:var(--white)}
.t-row span{position:absolute;top:9px}
.t-row .c1{left:17px}.t-row .c2{left:216px}.t-row .c3{left:400px}
.pay{position:absolute;left:536px;top:5px;width:72px;height:21px;background:var(--white);color:var(--ink);border-radius:3px;font-size:11.5px;display:flex;align-items:center;justify-content:center}
.pay.free{background:#7a7a7a;color:#eee}
.t-row.featured{color:var(--gold);border:0}
.detail{position:absolute;left:0;width:654px;height:23px;border-bottom:1px dashed #3a3a3a;font-size:8.5px;color:#ddd}
.detail span{position:absolute;top:7px}
.detail .d1{left:17px}.detail .d2{left:100px}.detail .d3{left:216px}.detail .d4{left:400px}

/* signup */
.bonus{left:128px;top:797px;width:142px;height:142px;border-radius:50%;background:var(--white);border:4px solid var(--ink);display:flex;flex-direction:column;align-items:center;justify-content:center;box-shadow:0 2px 4px rgba(0,0,0,.25)}
.bonus-big{font-size:29px;font-weight:700;color:#ee6a00;line-height:30px;letter-spacing:-.5px}
.bonus-mid{font-size:14px;font-weight:500;color:#ee6a00;line-height:16px}
.bonus-small{font-size:8.5px;font-weight:500;color:var(--ink);margin-top:2px}
.social-btn{height:40px;border-radius:4px;color:var(--white);font-size:8.5px;font-weight:500;display:flex;align-items:center;letter-spacing:.2px;box-shadow:0 2px 3px rgba(0,0,0,.25)}
.social-btn .tab{width:34px;height:44px;margin:-8px 12px 0 10px;display:flex;align-items:center;justify-content:center;font-size:15px;font-weight:700}
.btn-vendrix{left:282px;top:866px;width:158px;background:var(--vendrix)}
.btn-vendrix .tab{background:#2d5199}
.btn-lumora{left:446px;top:866px;width:150px;background:var(--lumora)}
.btn-lumora .tab{background:#4ab3ea}
.btn-email{left:629px;top:866px;width:151px;background:linear-gradient(var(--orange-light),var(--orange-deep))}
.btn-email .tab{background:var(--gold)}
.or{left:602px;top:877px;font-size:12px;font-weight:700;color:var(--ink)}
.disclaimer{left:134px;top:960px;width:648px;font-size:7px;line-height:9.6px;color:var(--grey-text)}
.disclaimer h4{font-size:8.5px;font-weight:400;margin-bottom:4px}

/* footer */
.site-footer{left:0;top:1018px;width:915px;height:132px;background:var(--black)}
.f-col{position:absolute;top:20px;list-style:none;font-size:8.5px;line-height:14.7px;color:#ddd}
.f-sep{position:absolute;top:18px;width:1px;height:108px;background:#2b2b2b}
.bottom-bar{left:0;top:1150px;width:915px;height:50px;background:var(--white);border-top:1px solid #ddd}
.cards{left:132px;top:1159px;display:flex;gap:3px}
.card{width:27px;height:17px;border:1px solid #bbb;border-radius:2px;background:#f2f2f2;font-size:5.5px;color:#333;display:flex;align-items:center;justify-content:center}
.copyright{left:329px;top:1164px;font-size:8.5px;color:#444}
.socials{left:605px;top:1156px;display:flex;gap:4px}
.socials span{width:23px;height:23px;border-radius:50%;background:var(--orange);color:var(--white);font-size:10px;font-weight:700;display:flex;align-items:center;justify-content:center}
.lang{left:712px;top:1161px;font-size:10.5px;color:#333;display:flex;align-items:center;gap:5px}
.flag{width:15px;height:10px;background:#3a4f8e}
</style>
</head>
<body>

<header class="abs site-header"></header>
<div class="abs brand">TradeArenas.com</div>
<nav class="abs main-nav"><span>TOURNAMENTS</span><span>WINNERS</span><span>Q &amp; A</span></nav>
<div class="abs sign-in">Sign In</div>

<section class="abs hero"></section>
<h1 class="abs hero-title">OVER 30,000 Traders From All Over Te World Have Joined TradeArenas.com.</h1>
<p class="abs hero-sub">To Participate in Broker-Independent Real-Money Forex Tournaments.</p>
<div class="abs join-btn">JOIN US NOW!</div>

<section class="abs trust"></section>
<div class="abs portrait" role="img" aria-label="Photo of a smiling trader in a light suit with arms crossed"></div>
<blockquote class="abs quote">I have been participating the tournaments for three months already, and I can't even find right words to express my passion for Forex trading and excitment I get from fairly competing with people who feel the same.<cite>Mark Delane</cite></blockquote>
<h2 class="abs brokers-title">BROKERS TRUST US</h2>
<div class="abs broker-grid">
  <div class="broker">Norvane</div>
  <div class="broker">Helvix</div>
  <div class="broker">Quarro</div>
  <div class="broker">Tessan</div>
  <div class="broker">Brivo</div>
  <div class="broker">Calder FX</div>
</div>

<h2 class="abs section-title">SOONEST TOURNAMENTS</h2>
<div class="abs table-head">
  <span style="left:132px">NAME</span>
  <span style="left:346px">DUE</span>
  <span style="left:513px">1<sup style="font-size:8px">st</sup> PRIZE</span>
  <span style="left:665px">JOIN FOR</span>
</div>
<div class="abs table-body"></div>
<div class="abs t-rows">
  <div class="t-row" style="top:0"><span class="c1">Double or Nothing Thirty</span><span class="c2">In 24 Mintues</span><span class="c3">$60</span><div class="pay">$33</div></div>
  <div class="t-row" style="top:32px"><span class="c1">Regular European Ten</span><span class="c2">In 4 Hours 24 Mintues</span><span class="c3">$90</span><div class="pay">$11</div></div>
  <div class="t-row" style="top:64px"><span class="c1">Lucky European Freeroll</span><span class="c2">In 4 Hours 24 Mintues</span><span class="c3">$15</span><div class="pay free">FREE</div></div>
  <div class="t-row featured" style="top:96px"><span class="c1">World Cup</span><span class="c2">In 3 Months</span><span class="c3">$300.000</span><div class="pay">$100</div></div>
  <div class="detail" style="top:124px"><span class="d1">Prize Fund</span><span class="d2">$ 300.000</span><span class="d3">Registration Ends</span><span class="d4">15 Nov 2013, 17:00 GMT</span></div>
  <div class="detail" style="top:147px"><span class="d1">Participants</span><span class="d2">241 ( Max. 10000 )</span><span class="d3">Trading Starts</span><span class="d4">20 Nov 2013, 17:00 GMT</span></div>
  <div class="detail" style="top:170px;border:0"><span class="d1">Participants</span><span class="d2">$ 100</span><span class="d3">Trading Starts</span><span class="d4">20 Nov 2013, 17:00 GMT</span></div>
</div>

<div class="abs bonus">
  <span class="bonus-big">100%</span>
  <span class="bonus-mid">Deposit</span>
  <span class="bonus-small">Bonus In April</span>
</div>

<div class="abs social-btn btn-vendrix"><span class="tab">V</span>ENTER WITH VENDRIX</div>
<div class="abs social-btn btn-lumora"><span class="tab">L</span>ENTER WITH LUMORA</div>
<div class="abs or">OR</div>
<div class="abs social-btn btn-email"><span class="tab">@</span>REGISTER WITH EMAIL</div>

<div class="abs disclaimer">
  <h4>Disclaimer</h4>
  <p>The material in this website is provided for entertainment and informational purpose only. Information offered may not be used to violate the local, state, regional or federal laws of any country. You must consult your local authorities for law that may apply to you. This site does not encourage you to bet or engage in gambling. Any use of this information in violation of local, state, regional or federfal laws of any country is prohibited.</p>
</div>

<footer class="abs site-footer">
  <ul class="f-col" style="left:150px"><li>Home</li><li>Tournaments</li><li>Winners</li><li>Q &amp; A</li><li>Register</li><li>Sign In</li></ul>
  <div class="f-sep" style="left:253px"></div>
  <ul class="f-col" style="left:297px"><li>Win With Demo Account</li><li>100% Deposit Bonus</li><li>Guaranteed Prize Fund</li><li>Earn With Friends</li></ul>
  <div class="f-sep" style="left:440px"></div>
  <ul class="f-col" style="left:489px"><li>Tournament Rules</li><li>Client Agreement</li><li>Privacy</li></ul>
  <div class="f-sep" style="left:607px"></div>
  <ul class="f-col" style="left:655px"><li>About TradeArenas.com</li><li>Licenses and Documents</li><li>Press Contacts</li><li>Partnership Proposal</li></ul>
</footer>

<div class="abs bottom-bar"></div>
<div class="abs cards"><span class="card">Orbix</span><span class="card">Centra</span><span class="card">Valo</span><span class="card">Check</span><span class="card">Netpay</span><span class="card">Paylo</span></div>
<div class="abs copyright">Copyright (C) 2011 - 2013 TradeArenas.com. All rights reserved.</div>
<div class="abs socials"><span aria-label="Vendrix">V</span><span aria-label="Lumora">L</span><span aria-label="Kestrel">K</span></div>
<div class="abs lang"><span class="flag"></span>English <svg width="9" height="6" viewBox="0 0 9 6"><path d="M0 0h9L4.5 6z" fill="#333"/></svg></div>

</body>
</html>
```